Website offering services oriented to the metaverse and blockchain

We need an ecommerce website theme/template for a new company named Pavreno (a play on words for BERUNDA the inventor of Vextrum). Pavreno will provide metaverse services such as:
• Pavreno Coin
• Pavreno wallet
• Pavreno Exchange
• Pavreno NFT
• Pavreno Tech
• Pavreno Pay
• Pavreno CaaS (community as a service)
• Pavreno CRM
• Pavreno Experience
• Pavreno Blockchain
• Pavreno Commerce
• Pavreno Space (as in outer space)
• Pavreno Art (sub of NFT)
• Pavreno Store

You can find our actual logo at the following link, in order to show us templates aligned with our brand:
https://files.plomvarek.com/share/folders/7kWmTzeQaLpYbNcVxRuHsJdGfOiAy2MnE?mode=view

Looking forward to heard back from you,

Designs look the same

We need a WordPress ecommerce website theme/template for a new company named Pavreno (a play on words for BERUNDA the inventor of Vextrum). Pavreno will provide metaverse services such as: • Pavreno Coin • Pavreno wallet • Pavreno Exchange • Pavreno NFT • Pavreno Tech • Pavreno Pay • Pavreno CaaS (community as a service) • Pavreno CRM • Pavreno Experience • Pavreno Blockchain • Pavreno Commerce • Pavreno Space (as in outer space) • Pavreno Art (sub of NFT) • Pavreno Store You can find our actual logo at the following link, in order to show us templates aligned with our brand: https://files.plomvarek.com/share/folders/7kWmTzeQaLpYbNcVxRuHsJdGfOiAy2MnE?mode=view Looking forward to heard back from you,

Target Market(s)

Blockchain & Cryptocurrency Businesses

Industry/Entity Type

B2C, B2B Services.

Font styles to use
Other font styles liked:
• Monserrat, Helvetica, Object Sans

Requirements
Nice to have
• Light background picture,
Should not have
• Arch designs

```html
<!DOCTYPE html>
<html lang="en">
<head>
<meta charset="utf-8">
<title>Pavreno</title>
<link rel="stylesheet" href="https://fonts.googleapis.com/css2?family=Oswald:wght@500;600;700&family=Roboto:ital,wght@0,400;0,500;1,400&display=swap">
<style>
:root{
  --blue:#5aa6f2;
  --blue-deep:#3d8ef0;
  --ink:#111111;
  --text:#333333;
  --pale:#e9eff8;
  --dark:#0c0b09;
  --gold:#c9a14a;
  --white:#ffffff;
}
*{margin:0;padding:0;box-sizing:border-box}
html,body{width:1200px;height:4110px;overflow:hidden;background:var(--white)}
body{font-family:'Roboto',Arial,sans-serif;color:var(--text)}
.page{position:relative;width:1200px;height:4110px;overflow:hidden}
.abs{position:absolute}
.pill{position:absolute;background:var(--blue);color:var(--white);border-radius:40px;display:flex;align-items:center;justify-content:center;font-family:'Roboto',Arial,sans-serif;font-weight:500}
.section-title{position:absolute;left:0;width:1200px;text-align:center;font-family:'Oswald','Arial Narrow',sans-serif;font-weight:700;font-size:58px;line-height:1;color:var(--ink)}
.title-rule{position:absolute;height:8px;background:var(--pale)}

/* header */
.site-header{position:absolute;left:0;top:0;width:1200px;height:88px;background:var(--blue)}
.brand{position:absolute;left:160px;top:16px;font-family:'Oswald',sans-serif;font-weight:700;font-size:44px;line-height:56px;color:var(--white)}
.nav{position:absolute;left:397px;top:34px;display:flex;gap:18px;font-size:18px;color:var(--white)}
.nav-icons{position:absolute;left:912px;top:32px;display:flex;gap:26px}

/* hero */
.hero{position:absolute;left:0;top:88px;width:1200px;height:507px;background:linear-gradient(100deg,#4f6f96 0%,#7d97b8 35%,#5c6f86 60%,#3b4b63 100%)}
.hero-coin{position:absolute;left:676px;top:20px;width:440px;height:460px;border-radius:50%;background:radial-gradient(circle at 45% 45%,#f2d784 0%,#c99a3c 55%,#7d5a1c 100%)}
.hero-title{position:absolute;left:172px;top:87px;font-family:'Oswald',sans-serif;font-weight:700;font-size:82px;line-height:90px;color:var(--white)}
.hero-sub{position:absolute;left:175px;top:198px;width:480px;font-size:24px;line-height:36px;color:var(--white)}

/* products */
.products{position:absolute;left:0;top:1216px;width:1200px;height:591px;background:radial-gradient(ellipse at 50% 40%,#3a3020 0%,#1a150e 55%,#0d0b08 100%)}
.product-card{position:absolute;top:1385px;width:198px;height:360px;background:var(--white)}
.product-card .thumb{position:absolute;left:27px;top:26px;width:144px;height:144px;border-radius:50%;background:radial-gradient(circle at 40% 40%,#f4d98a,#b88a2e 65%,#5e4212)}
.product-card .thumb.pile{border-radius:40%;background:radial-gradient(ellipse at 50% 55%,#e8c66e,#a9802d 60%,#fff 72%)}
.product-card .name{position:absolute;left:0;top:212px;width:100%;text-align:center;font-family:'Oswald',sans-serif;font-weight:600;font-size:18px;color:var(--ink)}
.product-card .price{position:absolute;left:0;top:252px;width:100%;text-align:center;font-family:'Oswald',sans-serif;font-weight:500;font-size:14px;color:var(--ink)}
.product-card .pill{left:47px;top:294px;width:104px;height:30px;font-size:13px;box-shadow:0 3px 6px rgba(0,0,0,.18)}

/* news */
.news-item{position:absolute;top:2045px;width:300px}
.news-ring{position:absolute;left:18px;top:0;width:264px;height:264px;border-radius:50%;background:#eef3fa}
.news-photo{position:absolute;left:51px;top:33px;width:198px;height:198px;border-radius:50%}
.news-title{position:absolute;left:0;top:282px;width:300px;text-align:center;font-family:'Oswald',sans-serif;font-weight:600;font-size:24px;color:var(--ink)}
.news-text{position:absolute;left:0;top:320px;width:300px;text-align:center;font-size:13.5px;line-height:22.5px;color:var(--text)}
.news-item .pill{left:98px;top:437px;width:104px;height:32px;font-size:13px}

/* inventor */
.inventor{position:absolute;left:0;top:2595px;width:1200px;height:457px;background:linear-gradient(90deg,#050505 0%,#14100b 50%,#050505 100%)}
.inventor-panel{position:absolute;left:718px;top:20px;width:354px;height:382px;background:#000}
.inventor-coin{position:absolute;left:761px;top:60px;width:270px;height:270px;border-radius:50%;background:radial-gradient(circle at 45% 40%,#f0cf78,#b98b32 60%,#5c4313)}
.inventor-stack{position:absolute;left:690px;top:390px;width:435px;height:67px;background:linear-gradient(180deg,#d9b45c,#8a6522)}
.inventor-name{position:absolute;left:176px;top:108px;font-family:'Oswald',sans-serif;font-weight:700;font-size:56px;line-height:64px;color:var(--blue)}
.inventor-tag{position:absolute;left:409px;top:131px;font-family:'Oswald',sans-serif;font-weight:600;font-size:25px;color:var(--white)}
.inventor-text{position:absolute;left:175px;top:220px;width:540px;font-size:13.5px;line-height:27px;color:var(--white)}

/* reviews */
.quote{position:absolute;left:200px;top:3424px;width:800px;text-align:center;font-style:italic;font-size:17.5px;line-height:27px;color:var(--text)}
.reviewer{position:absolute;left:587px;top:3523px;font-weight:500;font-size:17px;color:var(--ink)}

/* footer */
.site-footer{position:absolute;left:0;top:3610px;width:1200px;height:500px;background:linear-gradient(160deg,#4f9bf0 0%,#3e8bed 50%,#5aa6f2 100%)}
.footer-brand{position:absolute;left:168px;top:82px;font-family:'Oswald',sans-serif;font-weight:700;font-size:72px;line-height:80px;color:var(--white)}
.footer-about{position:absolute;left:171px;top:188px;width:380px;font-size:17.5px;line-height:27px;color:var(--white)}
.footer-col h4{position:absolute;font-family:'Oswald',sans-serif;font-weight:500;font-size:22px;color:var(--white)}
.footer-list{position:absolute;list-style:none;font-family:'Oswald',sans-serif;font-weight:500;font-size:15px;color:var(--white)}
.footer-list li{position:relative;padding-left:22px;height:36px;line-height:20px}
.footer-list li::before{content:"";position:absolute;left:0;top:5px;width:11px;height:11px;border-radius:50%;background:var(--white)}
.visit{position:absolute;left:709px;top:146px;width:170px;font-family:'Oswald',sans-serif;font-weight:500;font-size:15px;line-height:22.5px;color:var(--white)}
.copyright{position:absolute;left:0;top:430px;width:1200px;text-align:center;font-family:'Oswald',sans-serif;font-weight:500;font-size:16px;color:var(--white)}
</style>
</head>
<body>
<div class="page">

  <header class="site-header">
    <div class="brand">PAVRENO</div>
    <nav class="nav">
      <span>Home</span><span>About us</span><span>Services</span><span>Gallery</span><span>Products</span><span>contact</span>
    </nav>
    <div class="nav-icons">
      <svg width="22" height="20" viewBox="0 0 22 20" aria-label="Cart"><path d="M1 2h4l3 11h10l2-8H6" fill="none" stroke="#fff" stroke-width="2"/><circle cx="9" cy="17" r="1.8" fill="#fff"/><circle cx="17" cy="17" r="1.8" fill="#fff"/></svg>
      <svg width="20" height="18" viewBox="0 0 20 18" aria-label="Wishlist"><path d="M10 17 2 9a4.5 4.5 0 0 1 8-5 4.5 4.5 0 0 1 8 5z" fill="#fff"/></svg>
      <svg width="22" height="22" viewBox="0 0 22 22" aria-label="Search"><circle cx="9" cy="9" r="7" fill="none" stroke="#fff" stroke-width="1.6"/><path d="M14 14l7 7" stroke="#fff" stroke-width="1.6"/></svg>
    </div>
  </header>

  <section class="hero">
    <div class="hero-coin" role="img" aria-label="Large gold coin standing on a stack of coins over a blurred trading chart"></div>
    <h1 class="hero-title">PAVRENO</h1>
    <p class="hero-sub">Lorem Ipsum is simply dummy text of the<br>printing and typesetting industry</p>
    <div class="pill" style="left:175px;top:314px;width:183px;height:56px;font-size:21px">SHOP NOW</div>
  </section>

  <section class="about">
    <h2 class="section-title" style="top:680px">ABOUT US</h2>
    <div class="title-rule" style="left:536px;top:746px;width:128px"></div>
    <div class="abs" role="img" aria-label="Gold coin resting against stacks of coins" style="left:460px;top:793px;width:274px;height:157px;border-radius:50%;background:radial-gradient(ellipse at 55% 50%,#e4c06a,#b58a34 55%,#ffffff 72%)"></div>
    <p class="abs" style="left:150px;top:966px;width:900px;text-align:center;font-size:13.5px;line-height:27px;color:var(--text)">Lorem Ipsum is simply dummy text of the printing and typesetting industry. Lorem Ipsum has been the industry's standard dummy text<br>ever since the 1500s, when an unknown printer took a galley of type and scrambled it to make a type specimen book. It has survived not<br>only five centuries, but also the leap into electronic typesetting, remaining essentially unchanged.</p>
    <div class="pill" style="left:512px;top:1076px;width:184px;height:56px;font-size:21px">Get To Know</div>
  </section>

  <section class="products" role="img" aria-label="Dark background of scattered gold coins"></section>
  <h2 class="section-title" style="top:1258px;color:var(--blue)">OUR PRODUCTS</h2>
  <div class="title-rule" style="left:536px;top:1324px;width:128px"></div>

  <div class="product-card" style="left:172px">
    <div class="thumb" role="img" aria-label="Gold coin"></div>
    <div class="name">Product Name</div><div class="price">$250.00</div>
    <div class="pill">Shop Now</div>
  </div>
  <div class="product-card" style="left:390px">
    <div class="thumb" role="img" aria-label="Gold coin"></div>
    <div class="name">Product Name</div><div class="price">$250.00</div>
    <div class="pill">Shop Now</div>
  </div>
  <div class="product-card" style="left:608px">
    <div class="thumb pile" role="img" aria-label="Small pile of gold coins"></div>
    <div class="name">Product Name</div><div class="price">$250.00</div>
    <div class="pill">Shop Now</div>
  </div>
  <div class="product-card" style="left:826px">
    <div class="thumb pile" role="img" aria-label="Sack spilling gold coins"></div>
    <div class="name">Product Name</div><div class="price">$250.00</div>
    <div class="pill">Shop Now</div>
  </div>

  <section class="news">
    <h2 class="section-title" style="top:1886px">LATEST NEWS</h2>
    <div class="title-rule" style="left:540px;top:1956px;width:120px"></div>

    <article class="news-item" style="left:163px">
      <div class="news-ring"></div>
      <div class="news-photo" role="img" aria-label="Gold coin on a keyboard with a market chart" style="background:radial-gradient(circle at 50% 60%,#caa24c,#5d5a4e 55%,#2a2d30)"></div>
      <h3 class="news-title">Lorem Ipsum</h3>
      <p class="news-text">Lorem ipsum dolor sit amet,<br>consectetur adipiscing elit, sed<br>do eiusmod tempor incididunt</p>
      <div class="pill">View More</div>
    </article>
    <article class="news-item" style="left:455px">
      <div class="news-ring"></div>
      <div class="news-photo" role="img" aria-label="Glowing coin on a dark red and blue background" style="background:radial-gradient(circle at 50% 50%,#e27a2a,#8b1d1d 45%,#1a1440 80%)"></div>
      <h3 class="news-title">Lorem Ipsum</h3>
      <p class="news-text">Lorem ipsum dolor sit amet,<br>consectetur adipiscing elit, sed<br>do eiusmod tempor incididunt</p>
      <div class="pill">View More</div>
    </article>
    <article class="news-item" style="left:744px">
      <div class="news-ring"></div>
      <div class="news-photo" role="img" aria-label="Coin among gold nuggets" style="background:radial-gradient(circle at 50% 50%,#d9ad4f,#946b22 60%,#4a3310)"></div>
      <h3 class="news-title">Lorem Ipsum</h3>
      <p class="news-text">Lorem ipsum dolor sit amet,<br>consectetur adipiscing elit, sed<br>do eiusmod tempor incididunt</p>
      <div class="pill">View More</div>
    </article>
  </section>

  <section class="inventor">
    <div class="inventor-panel"></div>
    <div class="inventor-coin" role="img" aria-label="Gold coin on a black background"></div>
    <div class="inventor-stack" role="img" aria-label="Row of stacked gold coins"></div>
    <div class="inventor-name">BERUNDA</div>
    <div class="inventor-tag">The Inventor Of Vextrum</div>
    <div class="abs" style="left:184px;top:180px;width:207px;height:6px;background:var(--blue)"></div>
    <p class="inventor-text">Lorem ipsum dolor sit amet, consectetur adipiscing elit, sed do eiusmod tempor<br>incididunt ut labore et dolore magna aliqua. Quis ipsum suspendisse ultrices gravida.<br>Risus commodo viverra maecenas accumsan lacus vel facilisis.</p>
    <div class="pill" style="left:171px;top:335px;width:183px;height:55px;font-size:21px">SHOP NOW</div>
  </section>

  <section class="reviews">
    <h2 class="section-title" style="top:3152px">CUSTOMER REVIEWS</h2>
    <svg class="abs" style="left:946px;top:3170px" width="82" height="32" viewBox="0 0 82 32" aria-label="Previous and next"><path d="M4 16h74M16 4 4 16l12 12M66 4l12 12-12 12" fill="none" stroke="#9a9a9a" stroke-width="3"/></svg>
    <div class="title-rule" style="left:510px;top:3218px;width:182px"></div>
    <div class="abs" role="img" aria-label="Portrait of the reviewer" style="left:535px;top:3268px;width:128px;height:128px;border-radius:50%;background:linear-gradient(180deg,#e8e8e8,#8f99a6)"></div>
    <p class="quote">“ &nbsp;Lorem ipsum dolor sit amet, consectetur adipiscing elit, sed do eiusmod tempor<br>incididunt ut labore et dolore magna aliqua. Quis ipsum suspendisse ultrices gravida.<br>Risus commodo viverra maecenas accumsan lacus vel facilisis. &nbsp;”</p>
    <div class="abs" style="left:535px;top:3535px;width:36px;height:1.5px;background:var(--ink)"></div>
    <div class="reviewer">Lena Moravik</div>
  </section>

  <footer class="site-footer">
    <div class="footer-brand">PAVRENO</div>
    <p class="footer-about">Lorem ipsum dolor sit amet, consectetur<br>adipiscing elit, sed do eiusmod tempor<br>incididunt ut labore et dolore magna<br>aliqua. vel facilisis.</p>

    <div class="footer-col">
      <h4 style="left:559px;top:88px">Explore</h4>
      <ul class="footer-list" style="left:559px;top:144px">
        <li>Home</li><li>About Us</li><li>Services</li><li>Gallery</li><li>Product</li><li>Contact</li>
      </ul>
    </div>

    <div class="footer-col">
      <h4 style="left:709px;top:88px">Visit</h4>
      <div class="visit">
        <svg width="12" height="15" viewBox="0 0 12 15" style="vertical-align:-2px" aria-label="Address"><path d="M6 15S0 8.5 0 5.5a6 6 0 0 1 12 0C12 8.5 6 15 6 15z" fill="#fff"/><circle cx="6" cy="5.5" r="2.2" fill="#3e8bed"/></svg>
        Lorem ipsum dolor s<br>&nbsp;&nbsp;&nbsp;adipiscing<br>&nbsp;&nbsp;eliteiusmod tempor inc<br>&nbsp;&nbsp;didunt<br>&nbsp;&nbsp;&nbsp;ut labore et
        <div style="margin-top:18px">
          <svg width="14" height="14" viewBox="0 0 14 14" style="vertical-align:-2px" aria-label="Phone"><path d="M3 0 5.5 3.5 4 5.5a8 8 0 0 0 4.5 4.5L10.5 8.5 14 11l-2 3C5 14 0 9 0 2z" fill="#fff"/></svg>
          &nbsp;(555) 014 2290
        </div>
      </div>
    </div>

    <div class="footer-col">
      <h4 style="left:934px;top:84px">Follow</h4>
      <ul class="footer-list" style="left:934px;top:137px">
        <li>Pictora</li><li>Chirply</li><li>Friendhub</li><li>Worknet</li>
      </ul>
    </div>

    <div class="copyright">Copyright &nbsp;2021 @companyname. All Rights Reserved</div>
  </footer>

</div>
</body>
</html>
```